Online Prescription Eyewear Company Needs a Website

We sell prescription glasses starting at $99 with Free Shipping. We have over 300 different styles and colors.

Our website is under construction and we need an amazing landing page to kick things off. Our brand is called VARNO and our website is called VARNOEYEWEAR.EXAMPLE.

We are a website similar to
kestonhale.example
shoprudyplume.example
Brova.example

We sell prescription glasses starting at $99 with Free Shipping. Options to upgrade to Anti Glare, Blue light Protection, Shadeshift or High Index.

We also have a lens replacement option and will change out old prescription lenses starting at $79 with Free Shipping.

Important!!

We Love the layout of https://tessbrundle.example/ . We are hoping to use Tess Brundle as a templet. The closest page that looks like Tess Brundle will win.

We do not prefer the pink. Substitute the pink with Navy Teal.

We also prefer a better footer than Tess Brundle

The landing page should include, Gender neutral and Colors are Black, White, Gray, Navy Teal

We prefer a Simple, Clean Look.

The Header should be similar to kestonhale.example

The Landing page look very similar to Tess Brundle with large banner with quad banner below to follow.

We need better footer. Here are the menu items for footer.

PRODUCTS
All Frames
Mens Frames
Womens Frames
Best Sellers
New Arrivals

ORDER
Single Vision Lenses
Blue Light Blocking Computer Lenses
High Index Lenses
Shadeshift Lenses
Reading Lenses

INFORMATION
Track Order
About Us
Contact Us
Returns
Warranty
FAQ

Target Market(s)

20-40 yo Male/Female wears glasses

Industry/Entity Type

Eyewear

Number of Pages Required

1 page

Font styles to use
Sans Serif

Colors
333333
5c5c5c
919191
b2b2b2
dfdfdf
f5f5f5
1b1b1b
474747
3276b5

Requirements
Must have
• The Landing page look very similar to Tess Brundle.
• Substitute the pink secondary color for Navy Teal
• Should have main Banner with Person wearing glasses. Then the quad banner below should highlight the box with glasses, glasses, etc.
Nice to have
• i have a pixel vault account, so if you find some awesome pictures I can purchase them if they fit in the site.

```html
<!DOCTYPE html>
<html lang="en">
<head>
<meta charset="utf-8">
<title>VARNO Eyewear</title>
<link rel="stylesheet" href="https://fonts.googleapis.com/css2?family=Montserrat:wght@400;500;600;700;800&family=Lora:wght@400;500&display=swap">
<style>
  :root{
    --teal:#1f4f66;
    --teal-dark:#183f52;
    --ink:#1b1b1b;
    --text:#333333;
    --muted:#5c5c5c;
    --soft:#919191;
    --line:#dfdfdf;
    --tile:#f5f5f5;
    --white:#ffffff;
  }
  *{box-sizing:border-box;margin:0;padding:0}
  html,body{width:824px;height:1200px;overflow:hidden;background:var(--white)}
  body{font-family:"Montserrat",sans-serif;color:var(--text);position:relative}

  .promo-bar{height:12px;background:var(--teal);color:var(--white);font-size:5.5px;letter-spacing:.4px;display:flex;align-items:center;justify-content:center}

  .site-header{height:38px;display:flex;align-items:center;padding:0 160px;border-bottom:1px solid var(--line)}
  .brand{font-weight:600;font-size:15px;letter-spacing:3px;color:var(--ink);display:flex;align-items:center;gap:5px}
  .brand-dot{width:5px;height:5px;border-radius:50%;background:var(--teal)}
  .main-nav{display:flex;gap:18px;margin-left:40px;font-size:5.5px;font-weight:600;letter-spacing:.5px;color:var(--ink)}
  .header-tools{margin-left:auto;display:flex;gap:16px;align-items:center;font-size:5.5px;font-weight:600;letter-spacing:.5px;color:var(--ink)}
  .header-tools span{display:flex;align-items:center;gap:4px}

  .hero{position:relative;height:302px;background:linear-gradient(90deg,#f2f3f4 0%,#eceef0 55%,#f4f5f6 100%)}
  .hero-photo{position:absolute;left:118px;top:0;width:250px;height:302px;background:linear-gradient(180deg,#d9d4cf 0%,#c7bfb8 50%,#2b2b2b 100%);opacity:.55}
  .hero-tagline{position:absolute;left:402px;top:60px;height:160px;writing-mode:vertical-rl;transform:rotate(180deg);font-size:6.5px;letter-spacing:1.6px;color:var(--muted);font-weight:500}
  .hero-tagline b{color:var(--teal)}
  .hero-copy{position:absolute;left:470px;top:95px;color:var(--ink)}
  .hero-kicker{font-size:15px;font-weight:600;margin-bottom:5px}
  .hero-title{font-size:28px;font-weight:800;line-height:1.05;letter-spacing:.3px}
  .btn-shop{display:inline-block;margin-top:14px;background:var(--teal);color:var(--white);font-size:6.5px;font-weight:700;letter-spacing:1px;padding:8px 14px}
  .hero-dots{position:absolute;left:50%;bottom:24px;transform:translateX(-50%);display:flex;gap:6px}
  .hero-dots i{width:6px;height:6px;border-radius:50%;border:1px solid var(--teal)}
  .hero-dots i.active{background:var(--teal)}

  .quad{position:absolute;top:371px;left:160px;width:503px;display:grid;grid-template-columns:245px 245px;gap:13px}
  .tile{height:179px;background:var(--tile);display:flex;flex-direction:column;align-items:center;padding-top:38px}
  .tile-art{width:130px;height:46px;border-radius:4px}
  .tile h3{font-family:"Lora",serif;font-weight:400;font-size:13px;color:var(--ink);margin-top:20px}
  .tile p{font-size:5.5px;color:var(--soft);margin-top:4px}

  .site-footer{position:absolute;top:784px;left:0;width:824px;height:416px;background:var(--teal);color:var(--white)}
  .footer-brand{position:absolute;top:36px;left:0;width:100%;display:flex;justify-content:center}
  .footer-brand .brand{color:var(--white)}
  .footer-brand .brand-dot{background:var(--white)}
  .newsletter{position:absolute;top:66px;width:100%;text-align:center}
  .newsletter h2{font-family:"Lora",serif;font-weight:400;font-size:19px}
  .newsletter p{font-size:6px;color:#c6d3da;margin-top:8px}
  .signup{display:flex;justify-content:center;margin-top:14px}
  .signup .field{width:110px;height:17px;background:var(--white);color:var(--soft);font-size:5.5px;display:flex;align-items:center;padding-left:6px}
  .signup .btn{height:17px;background:var(--teal-dark);font-size:5.5px;font-weight:700;letter-spacing:.6px;padding:0 10px;display:flex;align-items:center;border:1px solid #3a6b82}
  .rule{position:absolute;left:160px;width:504px;height:1px;background:#3f6e85}
  .footer-cols{position:absolute;top:212px;left:165px;display:flex}
  .footer-col{width:212px}
  .footer-col h4{font-size:6.5px;font-weight:700;letter-spacing:.8px;margin-bottom:9px}
  .footer-col li{list-style:none;font-size:6px;color:#c6d3da;line-height:10.5px}
  .socials{position:absolute;top:362px;width:100%;display:flex;justify-content:center;gap:9px}
  .socials i{width:7px;height:7px;border-radius:50%;background:var(--white);opacity:.85}
  .copyright{position:absolute;top:382px;width:100%;text-align:center;font-size:5.5px;color:#c6d3da}
</style>
</head>
<body>
  <div class="promo-bar">Prescription Glasses starting at $99 with Free Shipping</div>

  <header class="site-header">
    <div class="brand">VARNO<span class="brand-dot"></span></div>
    <nav class="main-nav"><span>EYEWEAR</span><span>MENS</span><span>BEST SELLERS</span><span>NEW ARRIVALS</span></nav>
    <div class="header-tools">
      <span><svg width="7" height="7" viewBox="0 0 10 10"><circle cx="4" cy="4" r="3" fill="none" stroke="#1b1b1b" stroke-width="1.3"/><line x1="6.3" y1="6.3" x2="9" y2="9" stroke="#1b1b1b" stroke-width="1.3"/></svg>SEARCH</span>
      <span>SIGN IN</span>
      <span><svg width="9" height="8" viewBox="0 0 12 10"><path d="M0 1h2l1.5 6h6.5l1.5-4.5H3" fill="none" stroke="#1b1b1b" stroke-width="1.1"/><circle cx="4.5" cy="9" r=".9" fill="#1b1b1b"/><circle cx="9" cy="9" r=".9" fill="#1b1b1b"/></svg></span>
    </div>
  </header>

  <section class="hero">
    <div class="hero-photo" role="img" aria-label="Portrait of a person wearing prescription glasses"></div>
    <div class="hero-tagline">STARTING AT <b>$99</b> WITH FREE SHIPPING</div>
    <div class="hero-copy">
      <div class="hero-kicker">Prescription Glasses</div>
      <div class="hero-title">BE TRENDY<br>ELEGANT &amp;<br>IN STYLE</div>
      <span class="btn-shop">SHOP NOW</span>
    </div>
    <div class="hero-dots"><i class="active"></i><i></i><i></i></div>
  </section>

  <section class="quad">
    <article class="tile">
      <div class="tile-art" role="img" aria-label="Tortoiseshell eyeglass frames" style="background:linear-gradient(90deg,#c9bfae,#a89676,#c9bfae)"></div>
      <h3>New Arrivals</h3><p>Complete your look with our newest frames</p>
    </article>
    <article class="tile">
      <div class="tile-art" role="img" aria-label="Red and black cat-eye eyeglass frames" style="background:linear-gradient(90deg,#d6c2c2,#8a3a3a,#d6c2c2)"></div>
      <h3>Elegant and in style</h3><p>Complete your look with timeless frames</p>
    </article>
    <article class="tile">
      <div class="tile-art" role="img" aria-label="Clear transparent eyeglass frames" style="background:linear-gradient(90deg,#ececec,#d8d8d8,#ececec)"></div>
      <h3>Your fresh look!</h3><p>Complete your look with bright new frames</p>
    </article>
    <article class="tile">
      <div class="tile-art" role="img" aria-label="Glasses resting on an open gift box" style="background:linear-gradient(180deg,#d9d9d9,#2b2b2b)"></div>
      <h3>Get the hottest styles at 50% off</h3><p>Complete your look with our best sellers</p>
    </article>
  </section>

  <footer class="site-footer">
    <div class="footer-brand"><div class="brand">VARNO<span class="brand-dot"></span></div></div>
    <div class="newsletter">
      <h2>Get the latest news delivered daily!</h2>
      <p>Join us, enter your email and you will be always updated with the latest news in detail!</p>
      <div class="signup"><span class="field">Enter your email</span><span class="btn">SUBSCRIBE</span></div>
    </div>
    <div class="rule" style="top:178px"></div>
    <div class="footer-cols">
      <div class="footer-col"><h4>PRODUCTS</h4><ul><li>All Frames</li><li>Mens Frames</li><li>Womens Frames</li><li>Best Sellers</li><li>New Arrivals</li></ul></div>
      <div class="footer-col"><h4>ORDER</h4><ul><li>Single Vision Lenses</li><li>Blue Light Blocking Computer Lenses</li><li>High Index Lenses</li><li>Shadeshift Lenses</li><li>Reading Lenses</li></ul></div>
      <div class="footer-col"><h4>INFORMATION</h4><ul><li>Track Order</li><li>About Us</li><li>Contact Us</li><li>Returns</li><li>Warranty</li><li>FAQ</li></ul></div>
    </div>
    <div class="rule" style="top:344px"></div>
    <div class="socials"><i></i><i></i><i></i><i></i><i></i></div>
    <div class="copyright">© 2024 Varno. All Rights Reserved</div>
  </footer>
</body>
</html>
```